Business Cards for Tech Company - uBrightowl

We would like new modern business cards designed for our company. Attached are some examples of other business cards we like. <br/><br/>Info we need is: <br/>First Name, Last Name<br/>Address<br/>Store Phone<br/>Cell Phone<br/>Email Address<br/>Text Logo <br/>And Other Logo<br/>

Industry/Entity Type

Technology Equipment

Contact Information for Business Card

Please use these details as example:

Dale Morrow
Technology Specialist
Direct 555.617.2094
Phone 555-730-8186

dale.morrow@ubrightowl.example

2971 Willet Lane
Fernvale, OR 00427

Font styles to use
Sans Serif
Other font styles liked:
• Anything easy to read and modern

Colors

Designer to choose colors to be used in the design.

Requirements
Must have
• Both Logos
• Signature as name
• Use the text logo and use the shark logo but do not use the full shark logo. Have it where it is zoomed in and is expanding out of the card.
Nice to have
• Keep it clean and modern
• We like blue, white, and black/grays.
Should not have
• Random icons for phone and address.

```html
<!DOCTYPE html>
<html lang="en">
<head>
<meta charset="utf-8">
<title>uBrightowl Business Card</title>
<link rel="stylesheet" href="https://fonts.googleapis.com/css2?family=Lato:wght@400;700;900&display=swap">
<style>
  :root {
    --bg: #1e1f21;
    --blue: #1a6fe8;
    --blue-deep: #1d5fd6;
    --aqua: #3de6ea;
    --white: #ffffff;
    --ink: #1c1c1c;
    --gray: #6f6f6f;
    --teal-shade: #2a8c9a;
  }
  * { box-sizing: border-box; margin: 0; padding: 0; }
  html, body {
    width: 1200px; height: 900px; overflow: hidden;
    background: var(--bg);
    font-family: "Lato", sans-serif;
  }
  .stage { position: relative; width: 1200px; height: 900px; }
  .card {
    position: absolute; left: 300px; width: 600px; height: 343px;
    overflow: hidden; border-radius: 3px;
    box-shadow: 0 10px 30px rgba(0,0,0,.5);
  }
  .card-front {
    top: 70px;
    background: linear-gradient(200deg, var(--aqua) 0%, #2a9ff0 30%, var(--blue) 60%, var(--blue-deep) 100%);
  }
  .card-back { top: 487px; background: var(--white); }

  .emblem-art {
    position: absolute; right: 30px; top: 10px; width: 220px; height: 230px;
    border-radius: 50% 40% 50% 45%;
    background: radial-gradient(ellipse at 60% 55%, rgba(42,140,154,.85) 0%, rgba(42,140,154,.45) 55%, rgba(42,140,154,0) 75%);
  }
  .wordmark {
    position: absolute; font-weight: 900; letter-spacing: -1px; line-height: 1; white-space: nowrap;
  }
  .card-front .wordmark { left: 70px; top: 128px; font-size: 74px; color: var(--white); }
  .website {
    position: absolute; left: 0; right: 0; top: 268px; text-align: center;
    color: var(--white); font-size: 12px; font-weight: 700; letter-spacing: 3px;
  }

  .edge-band { position: absolute; width: 40px; height: 230px;
    background: linear-gradient(180deg, var(--blue) 0%, var(--blue) 45%, var(--aqua) 100%); }
  .edge-band-left { left: 0; bottom: 0; border-radius: 0 34px 34px 0; }
  .edge-band-right { right: 0; top: 0; border-radius: 34px 0 0 34px; }

  .card-back .wordmark { left: 0; right: 0; top: 58px; text-align: center; font-size: 64px; color: var(--gray); }

  .person { position: absolute; right: 330px; top: 205px; text-align: right; }
  .person-name { color: var(--blue); font-size: 20px; font-weight: 700; }
  .person-title { color: var(--gray); font-size: 12px; margin-top: 4px; }
  .divider { position: absolute; left: 290px; top: 180px; width: 1px; height: 100px; background: var(--gray); }

  .contact { position: absolute; left: 310px; top: 183px; list-style: none; }
  .contact li { display: flex; align-items: center; gap: 9px; font-size: 12px; color: var(--ink); height: 22px; white-space: nowrap; }
  .contact svg { width: 12px; height: 12px; fill: var(--gray); flex: none; }
  .contact .address { font-weight: 700; font-size: 13px; }
  .contact .address span { padding-left: 21px; }
</style>
</head>
<body>
<main class="stage">
  <section class="card card-front">
    <div class="emblem-art" role="img" aria-label="Brand emblem illustration emerging from the card edge"></div>
    <div class="wordmark">uBrightowl</div>
    <p class="website">www.ubrightowl.com</p>
  </section>

  <section class="card card-back">
    <div class="edge-band edge-band-left"></div>
    <div class="edge-band edge-band-right"></div>
    <div class="wordmark">uBrightowl</div>

    <div class="person">
      <p class="person-name">Dale Morrow</p>
      <p class="person-title">Technology Specialist</p>
    </div>
    <div class="divider"></div>

    <ul class="contact">
      <li><svg viewBox="0 0 12 12"><path d="M1 3c0-1 1-2 5-2s5 1 5 2v1H8V3H4v1H1zM3 5h6l2 5H1z"/></svg>555-730-8186</li>
      <li><svg viewBox="0 0 12 12"><path d="M3 0h6v12H3zM4 1v9h4V1z"/></svg>555.617.2094</li>
      <li><svg viewBox="0 0 12 12"><path d="M0 2h12v8H0zM1 3l5 4 5-4z"/></svg>dale.morrow@ubrightowl.example</li>
      <li class="address"><span>2971 Willet Lane, Fernvale, OR 00427</span></li>
    </ul>
  </section>
</main>
</body>
</html>
```